I have just launched a labour hire company and lookingfor a fresh vibrant website design

I need a landing page, a description of our services and capability, as well as an enquiries link, and register candidates link. My company is called Halvora recruitment and we supply labourers, excavator operators, and machine operators to the Civil and railway industries. I would like to stick to our logo theme and colours of Bright green, although I want a brighter green please than what I have. I have attached Images I like as well plaese. I do need a much bigger website eventually.

```html
<!DOCTYPE html>
<html lang="en">
<head>
<meta charset="utf-8">
<title>Halvora Recruitment</title>
<link href="https://fonts.googleapis.com/css2?family=Syncopate:wght@400;700&family=Poppins:wght@400;500;600&display=swap" rel="stylesheet">
<style>
:root{
  --green:#1a8a2a;
  --bright:#2bb83f;
  --dark:#1c1712;
  --ink:#111;
  --white:#fff;
  --grey:#444;
}
*{box-sizing:border-box;margin:0;padding:0}
html,body{width:1200px;height:3653px;overflow:hidden;background:var(--white);font-family:"Poppins",sans-serif;color:var(--ink)}
a{color:inherit;text-decoration:none}
.page{position:relative;width:1200px;height:3653px}
.abs{position:absolute}
.display{font-family:"Syncopate",sans-serif;text-transform:uppercase}
.accent{color:var(--green)}
.btn{position:absolute;display:flex;align-items:center;justify-content:center;gap:10px;background:var(--green);color:var(--white);font-weight:600;border-radius:30px;font-size:15px}
.btn svg{width:20px;height:16px}

/* header */
.site-header{left:0;top:0;width:1200px;height:91px;background:var(--white)}
.brand{display:flex;align-items:center;gap:12px}
.brand-mark{width:30px;height:30px;background:var(--bright)}
.brand-name{font-family:"Syncopate",sans-serif;font-weight:700;color:var(--ink);line-height:1.1}
.site-header .brand{position:absolute;left:110px;top:18px}
.site-header .brand-name{font-size:22px}
.site-header .brand-name small{display:block;font-size:11px;font-weight:400}
.main-nav{position:absolute;left:501px;top:41px;display:flex;gap:40px;font-size:14px;font-weight:500}
.main-nav .active{color:var(--green)}

/* hero */
.hero{left:0;top:91px;width:1200px;height:607px;background:linear-gradient(180deg,#5d5446 0%,#8a6c45 40%,#3b3226 100%)}
.hero h1{position:absolute;left:110px;top:145px;font-size:44px;line-height:60px;color:var(--white);font-weight:400}
.hero p{position:absolute;left:115px;top:275px;width:680px;color:var(--white);font-size:15.5px;line-height:30px;text-transform:uppercase;letter-spacing:.3px}
.hero-arrow{position:absolute;top:292px;width:56px;height:30px}

.band{position:absolute;background:var(--bright);height:31px}

/* about */
.about-back{left:119px;top:830px;width:470px;height:255px;background:var(--green);border-bottom-right-radius:60px}
.about-photo{left:89px;top:858px;width:468px;height:312px;background:linear-gradient(135deg,#6a8a9a,#b4a23c 60%,#4a4a3a)}
.about-text{left:640px;top:815px;width:446px}
.about-text h2{font-size:31px;font-weight:700;margin-bottom:18px}
.about-text p{font-size:14.5px;line-height:31px;color:var(--grey);text-align:justify}

/* supply */
.supply{left:0;top:1330px;width:1200px;height:568px;background:linear-gradient(180deg,#241d17,#3a2b1e 60%,#1d1610);border-bottom-left-radius:60px;border-bottom-right-radius:60px}
.section-title{position:absolute;left:0;width:1200px;text-align:center;font-size:30px;font-weight:700}
.supply-card{position:absolute;top:128px;width:311px;height:343px;border-bottom:6px solid var(--bright);border-bottom-right-radius:30px}
.supply-photo{width:100%;height:100%}
.supply-label{position:absolute;top:464px;height:56px;width:216px;background:var(--white);border-radius:16px;display:flex;align-items:center;justify-content:center;text-align:center;font-family:"Syncopate",sans-serif;font-size:17px;line-height:21px}

/* process */
.process-card{position:absolute;top:2044px;width:302px;height:320px;border:2px solid #ddd;border-radius:8px;background:var(--white);box-shadow:0 2px 6px rgba(0,0,0,.08);padding:0 36px}
.process-card svg.icon{display:block;margin:26px auto 0;width:72px;height:72px}
.process-card h3{font-family:"Syncopate",sans-serif;font-size:12px;font-weight:400;margin-top:20px}
.process-card p{font-size:13.5px;line-height:26.5px;color:var(--grey);margin-top:8px;text-align:justify}
.process-card .more{position:absolute;right:36px;bottom:10px;width:34px;height:18px}
.process-card.compact{padding:0 24px}
.process-card.compact svg.icon{margin-top:18px;width:64px;height:64px}
.process-card.compact h3{margin-top:14px}
.process-card.compact p{font-size:12.5px;line-height:25px;margin-top:6px}
.process-card.compact .more{right:24px;bottom:6px}
.side-arrow{position:absolute;width:44px;height:24px}

/* testimonials */
.testimonials{left:0;top:2492px;width:1200px;height:518px;background:var(--green)}
.quote-card{position:absolute;top:139px;width:475px;height:308px;border:2px solid var(--white);color:var(--white)}
.avatar{position:absolute;left:28px;top:14px;width:112px;height:112px;border-radius:50%;background:radial-gradient(circle,#e9cfa6,#8a6a48)}
.q-name{position:absolute;left:168px;top:62px;font-weight:600;font-size:16px;text-transform:uppercase}
.q-role{position:absolute;left:168px;top:86px;font-size:12px}
.stars{position:absolute;right:14px;top:62px;display:flex;gap:2px}
.stars svg{width:19px;height:19px}
.q-mark{position:absolute;left:0;width:100%;top:118px;text-align:center;font-size:60px;font-weight:700;line-height:50px}
.q-body{position:absolute;left:38px;right:20px;top:168px;font-size:13.5px;line-height:28px}

/* footer */
.site-footer{left:0;top:3120px;width:1200px;height:533px;background:var(--dark)}
.doubts{left:112px;top:3041px;width:976px;height:168px;background:var(--white);border:2px solid #ddd;border-radius:8px}
.doubts h2{position:absolute;left:0;width:100%;top:40px;text-align:center;font-size:29px;font-weight:700}
.site-footer .brand{position:absolute;left:425px;top:168px}
.site-footer .brand-mark{width:44px;height:44px}
.site-footer .brand-name{color:var(--white);font-size:33px}
.site-footer .brand-name small{display:block;font-size:16px;font-weight:400}
.foot-nav{position:absolute;left:0;width:1200px;top:282px;display:flex;justify-content:center;gap:46px;color:var(--white);font-family:"Syncopate",sans-serif;font-size:16px}
.social{position:absolute;left:524px;top:336px;display:flex;gap:8px}
.social span{width:26px;height:26px;background:var(--white);border-radius:5px}
.contact-item{position:absolute;top:404px;display:flex;align-items:center;gap:18px;color:var(--white);font-size:16px;line-height:20px}
.contact-item .ico{width:36px;height:32px;background:var(--bright);display:flex;align-items:center;justify-content:center}
.contact-item svg{width:20px;height:20px}
.foot-rule{position:absolute;left:112px;top:472px;width:976px;height:1px;background:#777}
.copyright{position:absolute;left:0;width:1200px;top:490px;text-align:center;color:var(--white);font-family:Georgia,serif;font-size:14px}
</style>
</head>
<body>
<div class="page">

<header class="abs site-header">
  <div class="brand"><span class="brand-mark"></span><span class="brand-name">HALVORA<small>RECRUITMENT PTY LTD</small></span></div>
  <nav class="main-nav"><a class="active" href="#home">HOME</a><a href="#about">ABOUT US</a><a href="#process">PROCESS</a><a href="#testimonials">TESTIMONIALS</a><a href="#enquiries">CONTACT US</a></nav>
</header>

<section class="abs hero" id="home" role="img" aria-label="Excavators on a construction site at sunset">
  <h1 class="display">Welcome to<br>Halvora <span style="color:var(--bright)">R</span>ecruitment</h1>
  <p>Lorem ipsum dolor sit amet, consectetur adipiscing elit, sed do eiusmod tempor incididunt ut labore et dolore magna aliqua.</p>
  <a class="btn" href="#register-candidates" aria-label="Register as a candidate" style="left:110px;top:388px;width:185px;height:43px">GET STARTED <svg viewBox="0 0 20 16"><path d="M3 2l6 6-6 6M10 2l6 6-6 6" stroke="#fff" stroke-width="2" fill="none"/></svg></a>
  <svg class="hero-arrow" style="left:24px" viewBox="0 0 56 30"><path d="M54 15H4M16 3L4 15l12 12" stroke="#fff" stroke-width="4" fill="none"/></svg>
  <svg class="hero-arrow" style="left:1104px" viewBox="0 0 56 30"><path d="M2 15h50M40 3l12 12-12 12" stroke="#fff" stroke-width="4" fill="none"/></svg>
</section>

<div class="band" style="left:0;top:709px;width:570px"></div>

<div class="abs about-back"></div>
<div class="abs about-photo" role="img" aria-label="Worker in hi-vis vest standing in front of a loader"></div>
<section class="abs about-text" id="about">
  <h2 class="display">About <span class="accent">Us</span></h2>
  <p>Halvora Recruitment is a NSW labour hire agency specialising in the civil sector. With a strong track record of providing skilled and reliable workers to the civil and rail construction industry, we have established ourselves as a trusted partner for companies seeking efficient and cost-effective staffing solutions. Our team of experienced professionals is dedicated to meeting the specific needs of our clients, ensuring seamless project execution and successful outcomes.</p>
</section>
<a class="btn" href="#about" style="left:640px;top:1164px;width:158px;height:37px;font-size:14px">READ MORE <svg viewBox="0 0 20 16"><path d="M3 2l6 6-6 6M10 2l6 6-6 6" stroke="#fff" stroke-width="2" fill="none"/></svg></a>

<div class="band" style="left:634px;top:1293px;width:566px"></div>

<section class="abs supply">
  <h2 class="section-title display" style="top:56px;color:var(--white)">We <span style="color:var(--bright)">Supply</span></h2>
  <div class="supply-card" style="left:112px;top:128px"><div class="supply-photo" role="img" aria-label="Labourer in hard hat beside an excavator" style="background:linear-gradient(160deg,#8fb3d0,#d2a93a 55%,#4a4a3a)"></div></div>
  <div class="supply-card" style="left:443px;top:136px"><div class="supply-photo" role="img" aria-label="Operator seated in an excavator cab" style="background:linear-gradient(160deg,#7d8a96,#3c4650 50%,#b07040)"></div></div>
  <div class="supply-card" style="left:774px;top:136px"><div class="supply-photo" role="img" aria-label="Two machine operators in hard hats at a control panel" style="background:linear-gradient(160deg,#6a7260,#c8c040 55%,#3a3a30)"></div></div>
  <div class="supply-label" style="left:156px">LABOURERS</div>
  <div class="supply-label" style="left:487px;top:470px">EXCAVATOR<br>OPERATORS</div>
  <div class="supply-label" style="left:818px;top:470px">MACHINE<br>OPERATORS</div>
</section>

<h2 class="section-title display" id="process" style="top:1976px">The <span class="accent">Process</span></h2>
<svg class="side-arrow" style="left:32px;top:2196px" viewBox="0 0 44 24"><path d="M42 12H4M14 2L4 12l10 10" stroke="#111" stroke-width="3.5" fill="none"/></svg>
<svg class="side-arrow" style="left:1122px;top:2196px" viewBox="0 0 44 24"><path d="M2 12h38M30 2l10 10-10 10" stroke="#111" stroke-width="3.5" fill="none"/></svg>

<div class="process-card" style="left:119px">
  <svg class="icon" viewBox="0 0 72 72" fill="none" stroke="#1a8a2a" stroke-width="3"><circle cx="36" cy="36" r="12"/><path d="M45 45l14 14"/><circle cx="14" cy="12" r="6"/><path d="M4 30c0-8 20-8 20 0"/><circle cx="58" cy="12" r="6"/><path d="M48 30c0-8 20-8 20 0"/><circle cx="14" cy="50" r="6"/><path d="M4 68c0-8 20-8 20 0"/></svg>
  <h3>RIGOROUS SELECTION PROCESS</h3>
  <p>Halvora Recruitment employs a meticulous selection process to identify and choose the most qualified and experienced civil labourers and operators.</p>
  <svg class="more" viewBox="0 0 34 18"><path d="M1 9h30M23 2l8 7-8 7" stroke="#1a8a2a" stroke-width="2.5" fill="none"/></svg>
</div>
<div class="process-card" style="left:445px">
  <svg class="icon" viewBox="0 0 72 72" fill="none" stroke="#1a8a2a" stroke-width="3"><rect x="12" y="10" width="38" height="54" rx="4"/><rect x="22" y="5" width="18" height="9" rx="2" fill="#1a8a2a"/><path d="M20 26h4M30 26h12M20 38h4M30 38h12M20 50h4M30 50h8"/><circle cx="56" cy="42" r="10" fill="#1a8a2a"/><path d="M51 42l4 4 6-7" stroke="#fff"/></svg>
  <h3>COMPLIANCE VERIFICATION</h3>
  <p>The agency places a strong emphasis on compliance with industry regulations and standards. respective roles.</p>
  <svg class="more" viewBox="0 0 34 18"><path d="M1 9h30M23 2l8 7-8 7" stroke="#1a8a2a" stroke-width="2.5" fill="none"/></svg>
</div>
<div class="process-card compact" style="left:773px">
  <svg class="icon" viewBox="0 0 72 72" fill="none" stroke="#1a8a2a" stroke-width="3"><rect x="10" y="6" width="46" height="40" rx="2"/><circle cx="33" cy="20" r="6"/><path d="M22 38c0-10 22-10 22 0"/><path d="M50 44l14-24" stroke-width="4"/><circle cx="20" cy="58" r="8"/><path d="M32 54h22M32 62h18"/></svg>
  <h3>REFERENCE CHECKING</h3>
  <p>Halvora Recruitment understands the importance of reliable references. They conduct thorough reference checks on all candidates to validate their previous work history, performance, and reliability.</p>
  <svg class="more" viewBox="0 0 34 18"><path d="M1 9h30M23 2l8 7-8 7" stroke="#1a8a2a" stroke-width="2.5" fill="none"/></svg>
</div>

<div class="band" style="left:0;top:2454px;width:562px"></div>

<section class="abs testimonials" id="testimonials">
  <h2 class="section-title display" style="top:52px;color:var(--white)">Testimonials</h2>
  <svg class="side-arrow" style="left:34px;top:296px" viewBox="0 0 44 24"><path d="M42 12H4M14 2L4 12l10 10" stroke="#fff" stroke-width="3.5" fill="none"/></svg>
  <svg class="side-arrow" style="left:1122px;top:296px" viewBox="0 0 44 24"><path d="M2 12h38M30 2l10 10-10 10" stroke="#fff" stroke-width="3.5" fill="none"/></svg>
  <div class="quote-card" style="left:122px">
    <div class="avatar" role="img" aria-label="Portrait photo of the reviewer"></div>
    <div class="q-name">Maren Ostby</div>
    <div class="q-role">GENERAL MANAGER</div>
    <div class="stars"><svg viewBox="0 0 20 20"><path d="M10 1l2.6 6 6.4.6-4.9 4.3 1.5 6.4L10 15l-5.6 3.3 1.5-6.4L1 7.6 7.4 7z" fill="#f2c230"/></svg><svg viewBox="0 0 20 20"><path d="M10 1l2.6 6 6.4.6-4.9 4.3 1.5 6.4L10 15l-5.6 3.3 1.5-6.4L1 7.6 7.4 7z" fill="#f2c230"/></svg><svg viewBox="0 0 20 20"><path d="M10 1l2.6 6 6.4.6-4.9 4.3 1.5 6.4L10 15l-5.6 3.3 1.5-6.4L1 7.6 7.4 7z" fill="#f2c230"/></svg><svg viewBox="0 0 20 20"><path d="M10 1l2.6 6 6.4.6-4.9 4.3 1.5 6.4L10 15l-5.6 3.3 1.5-6.4L1 7.6 7.4 7z" fill="#f2c230"/></svg><svg viewBox="0 0 20 20"><path d="M10 1l2.6 6 6.4.6-4.9 4.3 1.5 6.4L10 15l-5.6 3.3 1.5-6.4L1 7.6 7.4 7z" fill="none" stroke="#f2c230" stroke-width="1.5"/></svg></div>
    <div class="q-mark">&rdquo;</div>
    <div class="q-body" style="left:38px;font-size:13px;line-height:27px">Halvora Recruitment prides itself on delivering top-quality civil labourers and operators to the NSW Civil and Railway industries. The agency specialises in providing highly skilled professionals such as excavator operators, loader operators, pozi track operators, and moxy operators.</div>
  </div>
  <div class="quote-card" style="left:624px">
    <div class="avatar" role="img" aria-label="Portrait photo of the reviewer"></div>
    <div class="q-name">Tobias Renn</div>
    <div class="stars"><svg viewBox="0 0 20 20"><path d="M10 1l2.6 6 6.4.6-4.9 4.3 1.5 6.4L10 15l-5.6 3.3 1.5-6.4L1 7.6 7.4 7z" fill="#f2c230"/></svg><svg viewBox="0 0 20 20"><path d="M10 1l2.6 6 6.4.6-4.9 4.3 1.5 6.4L10 15l-5.6 3.3 1.5-6.4L1 7.6 7.4 7z" fill="#f2c230"/></svg><svg viewBox="0 0 20 20"><path d="M10 1l2.6 6 6.4.6-4.9 4.3 1.5 6.4L10 15l-5.6 3.3 1.5-6.4L1 7.6 7.4 7z" fill="#f2c230"/></svg><svg viewBox="0 0 20 20"><path d="M10 1l2.6 6 6.4.6-4.9 4.3 1.5 6.4L10 15l-5.6 3.3 1.5-6.4L1 7.6 7.4 7z" fill="#f2c230"/></svg><svg viewBox="0 0 20 20"><path d="M10 1l2.6 6 6.4.6-4.9 4.3 1.5 6.4L10 15l-5.6 3.3 1.5-6.4L1 7.6 7.4 7z" fill="none" stroke="#f2c230" stroke-width="1.5"/></svg></div>
    <div class="q-mark">&rdquo;</div>
    <div class="q-body" style="left:34px;top:172px;line-height:31px">Lorem ipsum dolor sit amet, consectetur adipiscing elit, sed do eiusmod tempor incididunt ut labore et dolore magna aliqua. Ut enim ad minim veniam, quis nostrud exercitation ullamco laboris nisi ut aliquip ex ea commodo consequat.</div>
  </div>
</section>

<footer class="abs site-footer">
  <div class="brand"><span class="brand-mark"></span><span class="brand-name">HALVORA<small>RECRUITMENT PTY LTD</small></span></div>
  <nav class="foot-nav"><a href="#home">HOME</a><a href="#about">ABOUT US</a><a href="#process">PROCESS</a><a href="#testimonials">TESTIMONIALS</a><a href="#enquiries">CONTACT US</a></nav>
  <div class="social"><span></span><span></span><span></span><span></span></div>
  <div class="contact-item" style="left:122px">
    <span class="ico"><svg viewBox="0 0 20 20"><path d="M10 1a6 6 0 0 0-6 6c0 5 6 11 6 11s6-6 6-11a6 6 0 0 0-6-6z" fill="#fff"/><circle cx="10" cy="7" r="2.2" fill="#2bb83f"/></svg></span>
    <span>Halvora recruitment Llc<br>lorem ipsum, AP-12034</span>
  </div>
  <div class="contact-item" style="left:488px">
    <span class="ico"><svg viewBox="0 0 20 20"><path d="M4 2l4 1 1 4-2 2a11 11 0 0 0 4 4l2-2 4 1 1 4-2 2C9 18 2 11 2 4z" fill="#fff"/></svg></span>
    <span>0400 000 123</span>
  </div>
  <div class="contact-item" style="left:752px">
    <span class="ico"><svg viewBox="0 0 20 20"><rect x="2" y="4" width="16" height="12" fill="none" stroke="#fff" stroke-width="2"/><path d="M2 4l8 7 8-7" stroke="#fff" stroke-width="2" fill="none"/></svg></span>
    <span>hello@halvorarecruitment.com.au</span>
  </div>
  <div class="foot-rule"></div>
  <div class="copyright">&copy; Copyright 2023 Halvora recruitment. All Rights Reserved.</div>
</footer>

<section class="abs doubts" id="enquiries">
  <h2 class="display">Do you have eny doubts</h2>
  <a class="btn" href="#enquiries" aria-label="Send an enquiry" style="left:402px;top:96px;width:158px;height:37px;font-size:14px">CONTACT US <svg viewBox="0 0 20 16"><path d="M3 2l6 6-6 6M10 2l6 6-6 6" stroke="#fff" stroke-width="2" fill="none"/></svg></a>
</section>

<span id="register-candidates" class="abs" style="left:0;top:91px;width:1px;height:1px"></span>

</div>
</body>
</html>
```